verdant terraces simple classy business card design

my name is owen harlow and I run a gardening business aimed at high class verdant terraces. the business name is verdant terraces and our logo was designed on pixel forum .My clientel are anything from residential homes to businesses. I take pride in my work and know that I offer a service like no other in my area.
The business card will be used to represent my business and I want it to be not only rememberable, but simplistic and modern. Eye catching too. Of course I would like it relatable to gardening and appealing to the correct clientel - those being garden enthusiasts, prestigious homes and businesses that are after top of the line gardening services like no other on the market.
I am not a typical lawn mowing business so I don't want a typical card design that represents that. The gardens I work with are generally million dollar properties with owners who are very garden proud looking for upkeep and guidance from me along with sometimes whole new garden designs. I want the business cards to show to my clients that I take pride, as they do, in their garden. And I want them to know from my card that I am a professional, qualified horticulturist offering them a top of the line service for life. I want them to refer my business on. I want them to look at my business card and see class and professionalism in a modern unique bold way.
The card should be simple with the possibility of the logo on the front being embossed/debossed and my details on the back the card should have a organic garden feel it's very important to me that it is absolutely perfect
I am also very open to ideas and suggestions so look forward to seeing the designs. the business logo has been supplied with this project and I want the card to be double sided

Contact info is
Owen Harlow - Managing Director / Horticulturist
Phone : 0481 526 704
Email: owenharlow@verdantterraces.com.au

Target Market(s)

high class gardens residential and commercial

Industry/Entity Type

Gardener

Contact Information for Business Card

Contact info is
Phone : 0481 526 704

PLEASE MAKE CARD DOUBLE SIDED

Requirements
Must have
• organic simple classy modern feel
• must flow with the current logo that has been supplied with this project
• Double sided
• Must explain in a simple way that I deal with high end gardens and I'm a qualified horticulturist
Nice to have
• embossed debossed logo
Should not have
• shouldn't be to busy or cheap looking

```html
<!DOCTYPE html>
<html lang="en">
<head>
<meta charset="utf-8">
<title>Verdant Terraces – Business Card</title>
<link rel="stylesheet" href="https://fonts.googleapis.com/css2?family=Open+Sans:wght@400;600&display=swap">
<style>
  :root {
    --ink: #232a31;
    --leaf: #6f9a45;
    --leaf-light: #8fb565;
    --paper: #ffffff;
    --shade: #d9dcdc;
    --text: #3a3f44;
    --stage: #eceae6;
  }
  html, body {
    margin: 0;
    padding: 0;
    width: 1200px;
    height: 800px;
    overflow: hidden;
    background: var(--stage);
    font-family: "Open Sans", Arial, sans-serif;
  }
  .canvas {
    width: 1200px;
    height: 800px;
    display: flex;
    align-items: center;
    justify-content: center;
    gap: 40px;
  }
  .card {
    width: 540px;
    height: 310px;
    box-shadow: 0 6px 18px rgba(0,0,0,0.18);
    display: block;
  }
  .card text { font-family: "Open Sans", Arial, sans-serif; }
  .brand-name { font-size: 24px; font-weight: 400; letter-spacing: 3px; fill: var(--leaf-light); }
  .person-name { font-size: 21px; font-weight: 600; fill: var(--leaf-light); letter-spacing: 0.5px; }
  .person-role { font-size: 12px; font-weight: 400; fill: #c9ccce; }
  .contact-line { font-size: 13px; font-weight: 400; fill: var(--text); }
  .address-line { font-size: 13px; font-weight: 400; fill: #f2f5ee; letter-spacing: 0.5px; }
  .back-brand { font-size: 26px; font-weight: 400; letter-spacing: 4px; fill: #e9efe1; }
</style>
</head>
<body>
<main class="canvas">

  <!-- Details side -->
  <svg class="card card-details" viewBox="0 0 540 310" xmlns="http://www.w3.org/2000/svg" aria-label="Business card, details side">
    <rect class="field-ink" width="540" height="310" fill="var(--ink)"/>
    <polygon class="field-shade" points="312,0 540,0 540,146 160,216" fill="var(--shade)"/>
    <polygon class="field-paper" points="324,0 540,0 540,140 172,208" fill="var(--paper)"/>
    <polygon class="field-leaf" points="0,240 540,140 540,310 0,310" fill="var(--leaf)"/>
    <polygon class="field-ink-foot" points="0,290 200,310 0,310" fill="var(--ink)"/>

    <g class="brand">
      <circle cx="70" cy="52" r="7" fill="var(--leaf-light)"/>
      <text class="brand-name" x="86" y="61">VERDANT TERRACES</text>
    </g>

    <g class="person">
      <text class="person-name" x="36" y="130">OWEN HARLOW</text>
      <text class="person-role" x="36" y="150">Managing Director /</text>
      <text class="person-role" x="36" y="167">Horticulturist</text>
    </g>

    <g class="contacts">
      <text class="contact-line" x="488" y="64" text-anchor="end">0481 526 704</text>
      <text class="contact-line" x="488" y="96" text-anchor="end">owenharlow@verdantterraces.com.au</text>
      <text class="contact-line" x="488" y="124" text-anchor="end">www.verdantterraces.com</text>

      <g class="icon-phone" transform="translate(508,46)">
        <circle r="11" fill="var(--leaf-light)"/>
        <path d="M-4,-5 l2,-1 2,3 -1.5,1.5 q1,2.5 3.5,3.5 l1.5,-1.5 3,2 -1,2 q-6,1 -10,-5 q-1,-3 0.5,-4.5z" fill="#fff"/>
      </g>
      <g class="icon-mail" transform="translate(508,72)">
        <circle r="11" fill="var(--leaf-light)"/>
        <rect x="-6" y="-4" width="12" height="8" fill="#fff"/>
        <path d="M-6,-4 L0,1 L6,-4" fill="none" stroke="var(--leaf-light)" stroke-width="1.2"/>
      </g>
      <g class="icon-web" transform="translate(508,98)">
        <circle r="11" fill="var(--leaf-light)"/>
        <circle r="6" fill="none" stroke="#fff" stroke-width="1.3"/>
        <ellipse rx="2.6" ry="6" fill="none" stroke="#fff" stroke-width="1.1"/>
        <line x1="-6" y1="0" x2="6" y2="0" stroke="#fff" stroke-width="1.1"/>
      </g>
    </g>

    <g class="address">
      <circle cx="46" cy="272" r="11" fill="var(--ink)"/>
      <path d="M46,279 l-4,-7 a4.5,4.5 0 1 1 8,0z" fill="#fff"/>
      <circle cx="46" cy="270" r="1.6" fill="var(--ink)"/>
      <text class="address-line" x="66" y="276">SUPPLY ADDRESS</text>
    </g>
  </svg>

  <!-- Brand side -->
  <svg class="card card-brand" viewBox="0 0 540 310" xmlns="http://www.w3.org/2000/svg" aria-label="Business card, brand side">
    <rect class="field-ink" width="540" height="310" fill="var(--ink)"/>
    <polygon class="field-leaf" points="0,0 540,0 540,150 0,260" fill="var(--leaf)"/>
    <polygon class="field-paper" points="0,0 540,0 540,40 0,150" fill="var(--paper)"/>
    <text class="back-brand" x="270" y="180" text-anchor="middle">VERDANT TERRACES</text>
  </svg>

</main>
</body>
</html>
```